Makeup Brush Cover Labeling/Packaging

Launching a new brush cover product that is designed to cover the bristles of various sized makeup brushes to protect them from grime and debris. We are a small company that is looking to grow and this would be an excellent opportunity to grow with us! Our current website is: thelashmitten.com, but the updated version is to be released in December, 2013.

I am looking for packaging and labeling designs to show off the uniqueness of the PlumeSock. I am currently considering strong transparent sleeves with heat sealed edges and want the product to do the selling itself (aka it's important that the customer can see the product right away! and understand its use) but am not opposed to boxes, cylinders, pillow-shaped packaging, etc. The sky is the limit. The final design should feel sophisticated and creative, and should give the feel of 'luxury' as it is a luxury product.

The product comes in three sizes, see attachment for an idea of size mockup.

The final label design could be simple, picture a basic insert in a transparent sleeve (sleeve not pictured, just simple label), inspiration: http://theamberquilljournal.wordpress.com/2009/07/23/no-1/)

or it could be complex in color, font and style (I love the bold text, black background and color splashes here!), inspiration: http://www.boxmuselog.com/vertex-q-for-lumavel.html/#!prettyPhoto/1/

Also attaching a simple box with transparent window idea (if we go box, we'll have the window be most of the front of the packaging).

Reason: I really appreciate everyone's designs! I would like to see if this project can attract anymore to review. At this time I'm looking for a label and packaging and most designs are packaging only.

Target Market(s)

Women 20+, women who would purchase luxury 'add-on' items for their makeup kits. This should be a design you can picture placed in a Lumavel or Kirn store.

Industry/Entity Type

It Company

Font styles to use
Sans Serif

Requirements
Must have
• Should be both a labeling and packaging idea.

```html
<!DOCTYPE html>
<html lang="en">
<head>
<meta charset="utf-8">
<title>PlumeSock – Packaging</title>
<link rel="stylesheet" href="https://fonts.googleapis.com/css2?family=Raleway:wght@300&family=Montserrat:wght@800&display=swap">
<style>
  :root {
    --paper: #ffffff;
    --ink: #1c1c1c;
    --stage-left: #ece9df;
    --stage-mid: #e6e6e4;
    --stage-right: #d3d9e2;
    --box-black: #0b0b0b;
    --smoke-grey: #8d8d8d;
    --splash-red: #e0401e;
    --splash-teal: #1d7f8a;
    --splash-green: #b6d62c;
    --window: #ffffff;
    --fold-line: rgba(255,255,255,0.35);
  }
  html, body {
    margin: 0;
    padding: 0;
    overflow: hidden;
    background: var(--paper);
  }
  .sheet {
    position: relative;
    width: 840px;
    height: 1200px;
    background: var(--paper);
    overflow: hidden;
  }
  .brand-mark {
    position: absolute;
    top: 82px;
    left: 0;
    width: 840px;
    text-align: center;
    font-family: "Raleway", sans-serif;
    font-weight: 300;
    font-size: 30px;
    letter-spacing: 6px;
    color: var(--ink);
    margin: 0;
  }
  .stage {
    position: absolute;
    top: 175px;
    left: 0;
    width: 840px;
    height: 523px;
    background: linear-gradient(90deg, var(--stage-left), var(--stage-mid) 50%, var(--stage-right));
  }
  .box-front {
    position: absolute;
    width: 290px;
    height: 190px;
    display: flex;
    align-items: center;
    justify-content: center;
  }
  .box-front--mono {
    left: 180px;
    top: 200px;
    background: linear-gradient(120deg, var(--box-black) 25%, #3a3a3a 55%, var(--smoke-grey) 75%, #2a2a2a);
  }
  .box-front--colour {
    left: 380px;
    top: 110px;
    width: 270px;
    height: 175px;
    background: linear-gradient(125deg, var(--splash-red) 0%, var(--splash-teal) 35%, #27a2a3 60%, var(--splash-green) 90%);
  }
  .box-name {
    font-family: "Raleway", sans-serif;
    font-weight: 300;
    font-size: 13px;
    letter-spacing: 2px;
    color: #ffffff;
  }
  .dielines {
    position: absolute;
    top: 770px;
    left: 0;
  }
  .dieline-name {
    font-family: "Raleway", sans-serif;
    font-weight: 300;
    font-size: 9px;
    letter-spacing: 1.5px;
    fill: #ffffff;
  }
  .dieline-tagline {
    font-family: "Montserrat", sans-serif;
    font-weight: 800;
    font-size: 5px;
    letter-spacing: 0.5px;
    fill: #ffffff;
  }
</style>
</head>
<body>
<main class="sheet">
  <h1 class="brand-mark">PlumeSock</h1>

  <section class="stage" aria-label="Box fronts">
    <div class="box-front box-front--colour" role="img" aria-label="Colour powder splash artwork in red, teal and green on black">
      <span class="box-name">PlumeSock</span>
    </div>
    <div class="box-front box-front--mono" role="img" aria-label="Grey smoke powder artwork on black">
      <span class="box-name">PlumeSock</span>
    </div>
  </section>

  <svg class="dielines" width="840" height="360" viewBox="0 770 840 360" aria-label="Box dielines">
    <defs>
      <linearGradient id="art-colour" x1="0" y1="0" x2="1" y2="1">
        <stop offset="0" stop-color="var(--splash-red)"/>
        <stop offset="0.2" stop-color="#111"/>
        <stop offset="0.4" stop-color="var(--splash-teal)"/>
        <stop offset="0.6" stop-color="#2aa0a8"/>
        <stop offset="0.8" stop-color="var(--splash-green)"/>
        <stop offset="1" stop-color="#0b0b0b"/>
      </linearGradient>
      <linearGradient id="art-mono" x1="0" y1="0" x2="1" y2="1">
        <stop offset="0" stop-color="#111"/>
        <stop offset="0.4" stop-color="#555"/>
        <stop offset="0.55" stop-color="#bdbdbd"/>
        <stop offset="0.75" stop-color="#333"/>
        <stop offset="1" stop-color="#080808"/>
      </linearGradient>
      <g id="dieline-shape">
        <path d="M117 778 H373 V800 H400 V925 H373 V930 H117 V925 H90 V800 H117 Z"/>
        <path d="M117 930 H373 L380 948 H110 Z"/>
        <path d="M130 948 H362 V1095 L352 1118 H140 L130 1095 Z"/>
      </g>
    </defs>

    <g class="dieline dieline--colour" role="img" aria-label="Box dieline with colour powder splash artwork">
      <use href="#dieline-shape" fill="url(#art-colour)"/>
      <circle cx="246" cy="866" r="45" fill="var(--window)"/>
      <line x1="117" y1="800" x2="117" y2="925" stroke="var(--fold-line)" stroke-dasharray="2 2"/>
      <line x1="373" y1="800" x2="373" y2="925" stroke="var(--fold-line)" stroke-dasharray="2 2"/>
      <line x1="130" y1="1075" x2="362" y2="1075" stroke="var(--fold-line)" stroke-dasharray="2 2"/>
      <text class="dieline-tagline" x="246" y="940" text-anchor="middle">LOREM IPSUM COLOR SIT AMET.</text>
      <text class="dieline-name" x="246" y="1020" text-anchor="middle">PlumeSock</text>
    </g>

    <g class="dieline dieline--mono" transform="translate(360 0)" role="img" aria-label="Box dieline with grey smoke powder artwork">
      <use href="#dieline-shape" fill="url(#art-mono)"/>
      <rect x="117" y="930" width="256" height="18" fill="var(--box-black)"/>
      <circle cx="246" cy="866" r="45" fill="var(--window)"/>
      <line x1="117" y1="800" x2="117" y2="925" stroke="var(--fold-line)" stroke-dasharray="2 2"/>
      <line x1="373" y1="800" x2="373" y2="925" stroke="var(--fold-line)" stroke-dasharray="2 2"/>
      <line x1="130" y1="1075" x2="362" y2="1075" stroke="var(--fold-line)" stroke-dasharray="2 2"/>
      <text class="dieline-tagline" x="246" y="940" text-anchor="middle">LOREM IPSUM COLOR SIT AMET.</text>
      <text class="dieline-name" x="246" y="1020" text-anchor="middle">PlumeSock</text>
    </g>
  </svg>
</main>
</body>
</html>
```